New business card for Building services company

I own a small 1 person business which primarily works at heights. I gain access to my work areas via ladders and use safety harnesses. I conduct gutter cleaning, roof cleaning with a pressure cleaner(water blaster), ground level pressure cleaning (driveways, footpaths and walls), I also do small handy-man jobs & gardening/ tree trimming.

I have just had a logo designed by Sketch Harbor, which I will upload. I'd like to see the themes followed through.
I like the colour of aqua or the colours what is in the logo.

I live in tropical north Queensland in Cairns, Australia. It is where the rain forest meets the Verdant Shoal Reef. On average it is 30+ degrees C.
Updates

Hello all designers. Thankyou for all the submissions so far. The following are my business details which I need on the card-

PELIKOR Roof, Gutter & Pressure Cleaning Services.
Director -Dylan Morwick
Ph 0417 552 803
Email- roofcleaning@vexlonet.com.au
ABN -38 924 417 205

Please include the following services which my business conducts-
*Gutter Cleaning
*Pressure Cleaning- Roof's, Driveways etc
*Minor Roof, Gutter & Building Maintenance
*Garden waste removal & complex cleanups

Public Liability upto $10 Million
Working at Heights Cert.

Quote-                                     Date-

Hi everyone,  could you please ensure you have -"Quote" and "Date" on the card. I'll need space to hand write details on the card for the specific details.        

Requirements
Must have
• The logo attached must be included.
• The rear side of the card is dedicated to job quoted and price of the job.
• *Please include- Quote price, Quote date. etc
• Including the tasks I do at work around the side of the card- Gutter Cleaning; Roof Cleaning, Gutter Maintenance; Gardening; Pressure Cleaning Roof's, Driveways etc.
Nice to have
• The rear side to have a ladder

```html
<!DOCTYPE html>
<html lang="en">
<head>
<meta charset="utf-8">
<title>PELIKOR Business Card</title>
<link rel="stylesheet" href="https://fonts.googleapis.com/css2?family=Questrial&family=Open+Sans:wght@300;400&family=Roboto+Condensed:wght@300&display=swap">
<style>
  :root {
    --page: #e9eef0;
    --card: #d3e5e2;
    --card-light: #e3efed;
    --brand-blue: #2c3a9e;
    --teal: #2f8f7e;
    --teal-band: #3f9c8c;
    --teal-soft: #8cc4c4;
    --ink: #1f3b4d;
    --name-blue: #3d63a3;
    --grey: #4c5a60;
    --white: #ffffff;
  }
  * { margin: 0; padding: 0; box-sizing: border-box; }
  html, body { width: 1200px; height: 900px; overflow: hidden; background: var(--page); }
  body { position: relative; font-family: "Open Sans", sans-serif; }

  .card {
    position: absolute; left: 290px; width: 638px;
    background: var(--card); overflow: hidden;
    box-shadow: 6px 8px 14px rgba(0,0,0,0.35);
  }
  .card--front { top: 22px; height: 378px; }
  .card--back { top: 502px; height: 356px; }
  .card__facets { position: absolute; inset: 0; width: 100%; height: 100%; }
  .card > *:not(.card__facets) { position: absolute; }

  .brand {
    left: 60px; top: 72px; width: 380px;
    display: flex; align-items: flex-start; justify-content: center; gap: 10px;
  }
  .brand-name {
    font-family: "Questrial", sans-serif; font-size: 70px; line-height: 1;
    color: var(--brand-blue); letter-spacing: 1px;
  }
  .brand-mark { width: 16px; height: 16px; margin-top: 6px; background: var(--brand-blue); flex: none; }
  .brand-tagline {
    left: 70px; top: 177px; width: 360px; text-align: center;
    font-family: "Questrial", sans-serif; font-size: 13px; color: var(--brand-blue); letter-spacing: 0.1px;
  }
  .brand-call {
    left: 70px; top: 200px; width: 360px; text-align: center;
    font-family: "Questrial", sans-serif; font-size: 21px; color: var(--teal);
  }
  .person__name {
    left: 35px; top: 248px; font-family: "Questrial", sans-serif; font-size: 25px; color: var(--name-blue);
  }
  .person__role {
    left: 36px; top: 280px; font-family: "Questrial", sans-serif; font-size: 16px; color: var(--grey);
  }
  .contact-list { left: 406px; top: 242px; list-style: none; }
  .contact-list li {
    display: flex; align-items: center; height: 26px;
    font-family: "Roboto Condensed", sans-serif; font-weight: 300; font-size: 14px; color: var(--teal);
  }
  .contact-list svg { width: 14px; height: 14px; margin-right: 26px; }
  .contact-list .no-icon { padding-left: 40px; }

  .service-band {
    display: flex; align-items: center; justify-content: center;
    height: 26px; border-radius: 13px; background: var(--teal-band);
    font-family: "Roboto Condensed", sans-serif; font-weight: 300; font-size: 11.4px;
    color: var(--white); white-space: nowrap; letter-spacing: -0.35px;
  }
  .service-band span + span::before { content: "|"; margin: 0 2px; font-weight: 400; }
  .card--front .service-band { left: 6px; right: 6px; top: 335px; }
  .card--back .service-band { left: 4px; right: 6px; top: 261px; height: 34px; border-radius: 17px; font-size: 11.6px; }

  .back-title {
    left: 0; right: 0; top: 14px; text-align: center;
    font-family: "Questrial", sans-serif; font-size: 46px; color: var(--white); letter-spacing: 1px;
  }
  .back-line { left: 0; right: 0; text-align: center; font-weight: 400; }
  .back-line--sub { top: 86px; font-size: 19px; color: var(--teal-soft); font-weight: 300; }
  .back-line--services { top: 130px; font-size: 20px; color: var(--ink); }
  .back-line--call { top: 176px; font-size: 19px; color: var(--ink); }
  .back-line--email { top: 222px; font-size: 19px; color: var(--ink); }
  .credentials {
    left: 0; right: 0; top: 306px; text-align: center;
    font-size: 17px; line-height: 22px; color: var(--teal); font-weight: 300;
  }
  .write-in { top: 330px; display: flex; align-items: flex-end; font-size: 14px; color: var(--grey); }
  .write-in::after { content: ""; display: block; width: 100px; border-bottom: 1px solid var(--grey); margin-left: 2px; }
  .write-in--quote { left: 14px; }
  .write-in--date { left: 480px; }
</style>
</head>
<body>
  <section class="card card--front">
    <svg class="card__facets" viewBox="0 0 638 378" preserveAspectRatio="none" aria-hidden="true">
      <polygon points="0,0 150,378 0,378" fill="var(--card-light)" opacity="0.55"/>
      <polygon points="638,0 488,378 638,378" fill="var(--card-light)" opacity="0.55"/>
      <polygon points="0,0 638,0 319,378" fill="var(--card-light)" opacity="0.35"/>
    </svg>
    <div class="brand">
      <div class="brand-name">PELIKOR</div>
      <div class="brand-mark"></div>
    </div>
    <div class="brand-tagline">ROOF, GUTTER &amp; PRESSURE CLEANING SERVICES</div>
    <div class="brand-call">CALL 0417 552 803</div>
    <div class="person__name">Dylan Morwick</div>
    <div class="person__role">Director</div>
    <ul class="contact-list">
      <li>
        <svg viewBox="0 0 24 24"><path fill="var(--teal)" d="M6.6 10.8c1.4 2.8 3.8 5.1 6.6 6.6l2.2-2.2c.3-.3.7-.4 1-.2 1.1.4 2.3.6 3.6.6.6 0 1 .4 1 1V20c0 .6-.4 1-1 1C10.6 21 3 13.4 3 4c0-.6.4-1 1-1h3.5c.6 0 1 .4 1 1 0 1.3.2 2.5.6 3.6.1.3 0 .7-.2 1z"/></svg>
        0417 552 803
      </li>
      <li>
        <svg viewBox="0 0 24 24"><rect x="3" y="6" width="18" height="12" fill="none" stroke="var(--teal)" stroke-width="1.6"/><path d="M3 6l9 7 9-7M3 18l7-6M21 18l-7-6" fill="none" stroke="var(--teal)" stroke-width="1.6"/></svg>
        roofcleaning@vexlonet.com.au
      </li>
      <li class="no-icon">ABN -38 924 417 205</li>
    </ul>
    <div class="service-band">
      <span>Gutter Cleaning</span><span>Garden waste removal &amp; complex cleanups</span><span>Gutter &amp; Building Maintenance</span><span>Minor Roof</span><span>Pressure Cleaning Roof's</span><span>Driveways</span>
    </div>
  </section>

  <section class="card card--back">
    <svg class="card__facets" viewBox="0 0 638 356" preserveAspectRatio="none" aria-hidden="true">
      <polygon points="0,0 150,356 0,356" fill="var(--card-light)" opacity="0.55"/>
      <polygon points="638,0 488,356 638,356" fill="var(--card-light)" opacity="0.55"/>
      <polygon points="0,0 638,0 319,356" fill="var(--card-light)" opacity="0.35"/>
    </svg>
    <div class="back-title">PELIKOR</div>
    <div class="back-line back-line--sub">ROOF, GUTTER &amp; PRESSURE</div>
    <div class="back-line back-line--services">CELANING SERVICES</div>
    <div class="back-line back-line--call">CALL :&nbsp; 0417 552 803</div>
    <div class="back-line back-line--email">E-mail: roofcleaning@vexlonet.com.au</div>
    <div class="service-band">
      <span>Gutter Cleaning</span><span>Garden waste removal &amp; complex cleanups</span><span>Gutter &amp; Building Maintenance</span><span>Minor Roof</span><span>Pressure Cleaning Roof's</span><span>Driveways</span>
    </div>
    <div class="credentials">Public Liability upto $10 Million<br>Working at Heights Cert.</div>
    <div class="write-in write-in--quote">Quote:</div>
    <div class="write-in write-in--date">Date:</div>
  </section>
</body>
</html>
```